Website Design for Business Law Firm

We have a logo and now we would like a web site design for our new website. Our small firm provides creative and aggressive transactional (not litigation) legal services to advise healthcare, technology, internet-based and traditional companies and investors in such companies on healthcare, technology, financing, mergers/acquisitions, real estate and other transactions, legal compliance and general corporate and business matters.

We would like to see a website design that is professional and appropriate for executives, professionals, investors and government regulators to visit, that conveys professionalism and competence while being a little edgy and modern - no typical legal motifs such as gavels, books, or scales of justice. We advise businesses and investors and guide them through complicated issues quickly, capably and differently from other law firms. We are part of the business team and get things done.

The logo is attached, and we like gray as a color to complement it. The intention of the logo is to convey that in a storm or challenging time, people come to this firm, and people come to this firm when they need the power and disruption to change things or shake them up.

I have also enclosed a picture of our business card for consideration.

On the other hand, you can check out the current simple site at www.venhollow.example to see we have used a space motif in the past to evoke that we help create stars (the nebula featured there). This is not a necessary part of the new website and it may look better without it.

We appreciate your creativity and look forward to designs.

Industry/Entity Type

Business

Requirements
Must have
• We anticipate the following pages, and you may submit different ideas for the different pages:
• 1. Landing page
• 2. Services pages - healthcare, IT/Technology, general counsel services, financings, mergers/acquisitions, mediation/arbitration, procurement and productization
• 3. About Us including contact information
• Our name and contact information:
• Quellane Law Firm, P.C.
• 8716 SW 19th Ave.
• Portland, OR 97213
• phone: 971.555.0143
• fax: 971.555.0187
Nice to have
• Please consider designs that enhance the impressions we are looking for
Should not have
• Please no gavels, scales of justice, law books, or similar traditional legal imagery.

```html
<!DOCTYPE html>
<html lang="en">
<head>
<meta charset="utf-8">
<title>Quellane Law Firm, P.C.</title>
<link rel="stylesheet" href="https://fonts.googleapis.com/css2?family=Arimo:wght@400;700&display=swap">
<style>
:root{
  --ink:#111;
  --navy:#241c5c;
  --header-top:#2a2627;
  --header-bottom:#0f0d0e;
  --nav-light:#f4f6f6;
  --nav-mid:#c9d2d3;
  --teal:#5f7c85;
  --red:#e01b24;
  --panel:#dcdcdc;
  --panel-inner:#aab7b7;
  --footer:#2b2b2d;
  --white:#fff;
  --rule:#b5b5b5;
}
*{margin:0;padding:0;box-sizing:border-box}
html,body{width:1121px;height:1200px;overflow:hidden;background:var(--white)}
body{font-family:"Arimo",Helvetica,Arial,sans-serif;color:var(--ink);position:relative}
.site-header{position:absolute;left:0;top:0;width:1121px;height:168px;
  background:linear-gradient(var(--header-top),var(--header-bottom));border-top:11px solid #000}
.brand{position:absolute;left:362px;top:16px;width:395px;text-align:center;color:var(--white)}
.brand-name{display:block;font-size:60px;letter-spacing:12px;line-height:86px;font-weight:400}
.brand-sub{display:block;font-size:29px;line-height:34px;margin-top:6px}
.call{position:absolute;left:830px;top:86px;width:256px;text-align:center;color:var(--white);font-size:18px;line-height:22px}
.main-nav{position:absolute;left:0;top:168px;width:1121px;height:58px;
  background:linear-gradient(var(--nav-light),var(--nav-mid));border-bottom:8px solid var(--teal)}
.main-nav ul{list-style:none;display:flex;justify-content:center;padding-top:19px;padding-left:10px}
.main-nav li{font-size:16px;line-height:18px;padding:0 16px;border-left:1.5px solid #222}
.main-nav li:first-child{border-left:none}
.hero{position:absolute;left:0;top:226px;width:1121px;height:363px;
  background:linear-gradient(#1f1650 0%,#3a2f7a 45%,#6a6a94 68%,#2a2a3c 85%,#0f1018 100%)}
.hero-card{position:absolute;left:345px;top:76px;width:729px;height:208px;
  background:rgba(230,230,236,.88);border-left:25px solid var(--red)}
.hero-card p{position:absolute;left:13px;top:55px;width:640px;font-size:20px;line-height:25px}
.hero-shadow{position:absolute;left:0;top:589px}
.intro{position:absolute;left:155px;top:626px;width:640px}
.intro h1{font-weight:400;font-size:25px;color:var(--navy);line-height:32px}
.intro p{font-size:15.6px;line-height:19.6px;margin-left:37px;width:500px}
.intro .first{margin-top:23px}
.intro hr{border:none;border-top:1.5px solid var(--rule);margin:17px 0 18px 6px;width:632px}
.glance{position:absolute;left:837px;top:633px;width:247px;height:362px;background:var(--panel)}
.glance-body{position:absolute;left:14px;top:73px;width:220px;height:275px;background:var(--panel-inner)}
.glance h2{position:absolute;left:4px;top:20px;width:241px;height:53px;background:var(--navy);
  color:var(--white);font-weight:400;font-size:20px;line-height:53px;padding-left:19px;
  box-shadow:0 3px 4px rgba(0,0,0,.35)}
.glance ul{list-style:none;position:absolute;left:18px;top:107px;font-size:16px;line-height:19.6px;color:#111}
.glance li{padding-left:13px;text-indent:-13px}
.glance li::before{content:"• ";}
.site-footer{position:absolute;left:0;top:1059px;width:1121px;height:141px;background:var(--footer);
  border-top:12px solid var(--teal);color:var(--white);font-size:12.3px;line-height:15.5px}
.footer-address{position:absolute;left:271px;top:23px}
.footer-links{position:absolute;left:538px;top:23px;list-style:none}
.social{position:absolute;left:706px;top:25px;width:130px;text-align:center}
.social svg{display:block;margin-top:10px}
</style>
</head>
<body>
<header class="site-header">
  <div class="brand">
    <span class="brand-name">QUELLANE</span>
    <span class="brand-sub">QUELLANE LAW FIRM, P.C.</span>
  </div>
  <p class="call">Call to discuss your needs<br>971.555.0143</p>
</header>
<nav class="main-nav">
  <ul><li>Home</li><li>About</li><li>Services</li><li>Contact</li><li>Get Started</li><li>FAQs</li></ul>
</nav>
<section class="hero" role="img" aria-label="Night city skyline photograph beside a bay under a violet sky">
  <div class="hero-card">
    <p>Creative and aggressive transactional legal services for healthcare, technology, financing, mergers/acquisitions, real estate and other transactions, legal compliance and general corporate and business matters.</p>
  </div>
</section>
<svg class="hero-shadow" width="1121" height="24" viewBox="0 0 1121 24" aria-hidden="true">
  <defs><linearGradient id="shade" x1="0" y1="0" x2="0" y2="1"><stop offset="0" stop-color="#888"/><stop offset="1" stop-color="#fff" stop-opacity="0"/></linearGradient></defs>
  <path d="M0 0H1121V6Q560 26 0 6Z" fill="url(#shade)"/>
</svg>
<main class="intro">
  <h1>Pragmatic, Creative Services for Innovative Businesses</h1>
  <p class="first">Creative and aggressive transactional legal services for healthcare, technology, financing, mergers/acquisitions, real estate and other transactions, legal compliance and general corporate and business matters. Creative and aggressive transactional legal services for healthcare, technology, financing, mergers/acquisitions, real estate and other transactions, legal compliance and general corporate and business matters.</p>
  <hr>
  <p>Creative and aggressive transactional legal services for healthcare, technology, financing, mergers/acquisitions, real estate and other transactions, legal compliance and general corporate and business matters. Creative and aggressive transactional legal services for healthcare, technology, financing, mergers/acquisitions, real estate and other transactions, legal compliance and general corporate and business matters.</p>
</main>
<aside class="glance">
  <div class="glance-body"></div>
  <h2>Services at a Glance</h2>
  <ul>
    <li>Strategic Alliances</li>
    <li>Business Relationship</li>
    <li>Outsourcing</li>
    <li>Procurements - Buying or Selling</li>
    <li>Licensing and Technology Exploration</li>
    <li>Real Estate</li>
    <li>Contracts</li>
    <li>Dispute Resolution</li>
  </ul>
</aside>
<footer class="site-footer">
  <p class="footer-address">Quellane Law Firm, P.C.,<br>P.O. Box 5582, Portland, OR 97208<br>info@quellane.example<br>Phone: 971.555.0143<br>Fax:&nbsp;&nbsp;&nbsp;&nbsp; 971.555.0161</p>
  <ul class="footer-links"><li>Home</li><li>Privacy</li><li>Terms of Use</li><li>FAQs</li></ul>
  <div class="social">
    <p>We are Social</p>
    <svg width="130" height="36" viewBox="0 0 130 36" aria-hidden="true">
      <circle cx="29" cy="18" r="16" fill="#c8c8c8"/>
      <circle cx="65" cy="18" r="16" fill="#c8c8c8"/>
      <circle cx="101" cy="18" r="16" fill="#c8c8c8"/>
    </svg>
  </div>
</footer>
</body>
</html>
```